Visual design for database driven web application

Need a clean, professional looking visual design for a web application.

PLUME is the new standardized K-12 school testing program for the state of Texas. We are building an application named PLUME-Finder (clever, yeah?) that will allow teachers, school administrators, and others to EASILY sort through millions of records of student data and print or export reports showing just the information they need about their students.

The state currently doesn't provide a user-friendly way to do this. They provide a "data dump" spreadsheet that school administrators and teachers must figure out how to manipulate to get the data they need. We are building a Web-based tool that will make it super simple and easy for our users to get the data they need in a format that works for them.

I've created a basic wireframe of the main application screen in Vellum QD Max. I need you to "skin" the wireframe to make it look good. Your mockup will set the tone for branding and visual design throughout the site.

See the attached screenshots. There are a few variations of the screen that include dynamic panels that open & close. Start by designing just the main screen and if you have time, do one or two of the panels. Thanks!
Updates

Target Market(s)

K-12 education professionals (teachers, administrators) in the state of Texas

Industry/Entity Type

Building

Requirements
Must have
• Your mockups should include all of the features & content shown in the attached screenshots.

However, you don't have to show all 10 rows of data. You can just do the column headers and one row of data. (It would be repetitive and unnecessary to spend time re-creating the entire grid with all of that data just to show your visual styling.)

The design should reflect the following concepts:

- Texas
- Education
- Simplicity
- Helpfulness
- Trust
- Professionalism

If I select your design, I will want your design source files (Illustrator, Photoshop, etc.)
Nice to have
• A logo in the upper left corner for PLUME-Finder. The logo should definitely communicate the design concepts described under "must have."

```html
<!DOCTYPE html>
<html lang="en">
<head>
<meta charset="utf-8">
<title>PLUME-Finder – Student Data</title>
<link rel="stylesheet" href="https://fonts.googleapis.com/css2?family=Open+Sans:wght@400;600;700&display=swap">
<style>
:root{
  --bg-top:#1ea6bc;
  --bg-bottom:#2bb9d0;
  --rule:#a8dbe3;
  --logo:#e2f4f6;
  --ink-dark:#1d2b2f;
  --nav-link:#d3eff3;
  --search-fill:#4db6c6;
  --search-edge:#28808c;
  --search-btn:#3cc6dc;
  --tab-active:#147b88;
  --tab-idle:#2a9fb1;
  --panel:#e3f0f2;
  --head-cell:#b5dde3;
  --row-band:#c9ecf1;
  --cell-text:#2a9db3;
  --footer:#a3e0ea;
  --btn:#e7f4f6;
  --btn-text:#3a6f78;
  --muted:#8fbcc3;
  --show:#1d93a8;
  --select:#c6e8ee;
}
*{box-sizing:border-box;margin:0;padding:0}
html,body{width:1200px;height:803px;overflow:hidden}
body{
  position:relative;
  font-family:"Open Sans",Verdana,sans-serif;
  background:linear-gradient(180deg,var(--bg-top) 0%,var(--bg-top) 40%,var(--bg-bottom) 100%);
}
.brand{
  position:absolute;left:70px;top:56px;
  font-family:"Open Sans",Verdana,sans-serif;font-weight:600;
  font-size:38px;line-height:52px;letter-spacing:1px;color:var(--logo);
}
.welcome{position:absolute;left:594px;top:32px;font-size:15px;color:var(--ink-dark)}
.account-links{
  position:absolute;left:810px;top:32px;font-size:13px;font-weight:600;
  letter-spacing:1px;color:var(--nav-link);
}
.account-links span{margin:0 6px}
.tool-icons{position:absolute;left:1062px;top:22px;display:flex;gap:10px;align-items:center}
.tool-icons .divider{width:1px;height:20px;background:var(--nav-link)}
.search-box{
  position:absolute;left:811px;top:73px;width:253px;height:32px;
  background:var(--search-fill);border:1px solid var(--search-edge);
}
.search-box svg{position:absolute;right:2px;top:1px}
.search-btn{
  position:absolute;left:1075px;top:76px;width:91px;height:19px;
  background:var(--search-btn);border-radius:3px 10px 3px 3px;
  color:#fff;font-size:14px;font-weight:700;text-align:center;line-height:19px;
}
.search-option{
  position:absolute;left:923px;top:107px;font-size:13px;color:var(--nav-link);
  display:flex;gap:6px;align-items:center;letter-spacing:.5px;
}
.header-rule{position:absolute;left:0;top:142px;width:1200px;height:7px;background:var(--rule)}
.tab{
  position:absolute;top:195px;height:35px;width:205px;
  color:#e7f6f8;font-size:17px;text-align:center;line-height:35px;
}
.tab.instructions{left:105px;background:var(--tab-active)}
.tab.student-data{left:334px;width:204px;background:var(--tab-idle)}
.data-panel{
  position:absolute;left:36px;top:230px;width:1132px;height:453px;
  background:var(--panel);border-radius:3px;
}
.grid{position:absolute;left:14px;top:23px;width:1104px}
.row{
  display:grid;
  grid-template-columns:66px 64px 59px 115px 83px 118px 105px 117px 40px 122px 67px 126px;
  column-gap:2px;height:36.6px;align-items:center;
}
.row.head{height:34px;margin-bottom:4px}
.row.head div{background:var(--head-cell);height:34px;line-height:34px;font-size:15px;color:var(--ink-dark);text-align:center}
.row.band{background:var(--row-band)}
.row div{font-size:15px;color:var(--cell-text);text-align:center}
.pager{
  position:absolute;left:37px;top:694px;width:1131px;height:49px;
  background:var(--footer);border-radius:3px;
}
.page-label{position:absolute;left:44px;top:14px;font-size:15px;color:var(--ink-dark)}
.page-label b{font-weight:400;margin-left:8px}
.page-label .rest{color:var(--muted);font-size:15px}
.pager-btn{
  position:absolute;top:14px;width:109px;height:26px;background:var(--btn);
  color:var(--btn-text);font-size:15px;font-weight:700;text-align:center;line-height:26px;
}
.pager-btn.next{left:269px}
.pager-btn.prev{left:393px}
.show-label{position:absolute;left:883px;top:14px;font-size:15px;font-weight:700;color:var(--show)}
.show-select{
  position:absolute;left:945px;top:9px;width:84px;height:30px;background:var(--select);
  border-radius:4px;font-size:15px;font-weight:700;color:var(--ink-dark);line-height:30px;padding-left:17px;
}
.show-select svg{position:absolute;right:8px;top:4px}
</style>
</head>
<body>
<header>
  <div class="brand">PLUME-Finder</div>
  <div class="welcome">Welcome &nbsp;: Owen</div>
  <div class="account-links">My Profile <span>/</span>Logout</div>
  <div class="tool-icons">
    <svg width="22" height="20" viewBox="0 0 22 20" aria-label="Print">
      <rect x="5" y="1" width="12" height="7" fill="#fff"/>
      <rect x="1" y="7" width="20" height="9" rx="2" fill="#6fa86a"/>
      <rect x="5" y="13" width="12" height="6" fill="#fff" stroke="#4f7f4a"/>
    </svg>
    <div class="divider"></div>
    <svg width="20" height="22" viewBox="0 0 20 22" aria-label="Export">
      <rect x="1" y="1" width="16" height="18" fill="#24333a"/>
      <rect x="4" y="2" width="10" height="6" fill="#fff"/>
      <rect x="4" y="12" width="10" height="6" fill="#d8d8d8"/>
      <path d="M14 13h5l-2.5 4z" fill="#e8c22c"/>
    </svg>
  </div>
  <div class="search-box">
    <svg width="38" height="30" viewBox="0 0 38 30" aria-label="Search">
      <circle cx="16" cy="12" r="8" fill="none" stroke="#1c4d57" stroke-width="3"/>
      <line x1="22" y1="18" x2="32" y2="27" stroke="#1c4d57" stroke-width="4" stroke-linecap="round"/>
    </svg>
  </div>
  <div class="search-btn">Search</div>
  <div class="search-option">Search &nbsp;Option
    <svg width="24" height="14" viewBox="0 0 24 14"><path d="M1 1h22L12 13z" fill="none" stroke="#d3eff3" stroke-width="1.5"/></svg>
  </div>
  <div class="header-rule"></div>
</header>

<nav>
  <div class="tab instructions">Instructions</div>
  <div class="tab student-data">Sutent Data</div>
</nav>

<main class="data-panel">
  <div class="grid">
    <div class="row head">
      <div>Date</div><div>Grade</div><div>ESC</div><div>CDC#</div><div>District</div><div>Campus</div>
      <div>Last Name</div><div>First Name</div><div>MI</div><div>Student ID</div><div>Gender</div><div>DOB</div>
    </div>
    <div class="row"><div>411</div><div>9</div><div>10</div><div>9999999999</div><div>Example</div><div>Examble H S</div><div>Montero</div><div>ROSALIE</div><div>I</div><div>1234546734</div><div>F</div><div>28/03/1980</div></div>
    <div class="row band"><div>411</div><div>9</div><div>10</div><div>9999999999</div><div>Example</div><div>Examble H S</div><div>Montero</div><div>ROSALIE</div><div>I</div><div>1234546734</div><div>F</div><div>28/03/1980</div></div>
    <div class="row"><div>411</div><div>9</div><div>10</div><div>9999999999</div><div>Example</div><div>Examble H S</div><div>Montero</div><div>ROSALIE</div><div>I</div><div>1234546734</div><div>F</div><div>28/03/1980</div></div>
    <div class="row band"><div>411</div><div>9</div><div>10</div><div>9999999999</div><div>Example</div><div>Examble H S</div><div>Montero</div><div>ROSALIE</div><div>I</div><div>1234546734</div><div>F</div><div>28/03/1980</div></div>
    <div class="row"><div>411</div><div>9</div><div>10</div><div>9999999999</div><div>Example</div><div>Examble H S</div><div>Montero</div><div>ROSALIE</div><div>I</div><div>1234546734</div><div>F</div><div>28/03/1980</div></div>
    <div class="row band"><div>411</div><div>9</div><div>10</div><div>9999999999</div><div>Example</div><div>Examble H S</div><div>Montero</div><div>ROSALIE</div><div>I</div><div>1234546734</div><div>F</div><div>28/03/1980</div></div>
    <div class="row"><div>411</div><div>9</div><div>10</div><div>9999999999</div><div>Example</div><div>Examble H S</div><div>Montero</div><div>ROSALIE</div><div>I</div><div>1234546734</div><div>F</div><div>28/03/1980</div></div>
    <div class="row band"><div>411</div><div>9</div><div>10</div><div>9999999999</div><div>Example</div><div>Examble H S</div><div>Montero</div><div>ROSALIE</div><div>I</div><div>1234546734</div><div>F</div><div>28/03/1980</div></div>
    <div class="row"><div>411</div><div>9</div><div>10</div><div>9999999999</div><div>Example</div><div>Examble H S</div><div>Montero</div><div>ROSALIE</div><div>I</div><div>1234546734</div><div>F</div><div>28/03/1980</div></div>
    <div class="row band"><div>411</div><div>9</div><div>10</div><div>9999999999</div><div>Example</div><div>Examble H S</div><div>Montero</div><div>ROSALIE</div><div>I</div><div>1234546734</div><div>F</div><div>28/03/1980</div></div>
  </div>
</main>

<footer class="pager">
  <div class="page-label">Page : <b>1</b> <span class="rest">2 3 4........25</span></div>
  <div class="pager-btn next">Next</div>
  <div class="pager-btn prev">Previous</div>
  <div class="show-label">Show</div>
  <div class="show-select">10
    <svg width="22" height="22" viewBox="0 0 22 22"><path d="M2 9L11 1l9 8z M2 13l9 8 9-8z" fill="#3f5a60"/></svg>
  </div>
</footer>
</body>
</html>
```